Audit/Compliance company needs Business Card Template

We are after a Business Card Template that we can modify internally to update details as people change positions.
We are an Australian based company specalising in Auditing and Quality/OHS systems development. - See www.kelvaranorth.com.au for more information
We would like the desings to be based around our logo and colours assocaited with it (attached for your information) however we are very open as to how the cards are designed.
We are looking for something quite edgy and mordern but it must have a professional/compliance feel to it (if possible).
The main details we would like to include within the card template are:
Name
Position Title
Postal Address
Phone Number
Mobile Number
Email Address
Website
The cards will be printed through tally press on Glossy paper so it should reflect the requirements below
Full Bleed Size (starting document size)
90 x 52 mm
1062 x 615 pixels
Document Trim Size (final size after being cut)
87 x 49 mm
1028 x 579 pixels
Resolution
300 DPI

```html
<!DOCTYPE html>
<html lang="en">
<head>
<meta charset="utf-8">
<title>Kelvara North Audit &amp; Compliance – Business Card</title>
<link href="https://fonts.googleapis.com/css2?family=Open+Sans:wght@300;400;700&display=swap" rel="stylesheet">
<style>
  :root {
    --ink: #222222;
    --grey: #4d4d4d;
    --brand-grey: #4a4a4a;
    --orange: #f26e21;
    --orange-light: #fbb02a;
    --yellow: #ffd400;
    --white: #ffffff;
    --rule: #555555;
  }
  html, body {
    margin: 0;
    padding: 0;
    width: 1200px;
    height: 676px;
    overflow: hidden;
    background: var(--white);
  }
  .card {
    position: relative;
    width: 1200px;
    height: 676px;
    background: var(--white);
    font-family: "Open Sans", sans-serif;
    color: var(--grey);
  }
  .brand {
    position: absolute;
    left: 40px;
    top: 112px;
    display: flex;
    align-items: center;
  }
  .brand-dot {
    width: 128px;
    height: 128px;
    border-radius: 50%;
    background: var(--orange-light);
  }
  .brand-rule {
    width: 1px;
    height: 92px;
    background: var(--rule);
    margin: 0 14px 0 40px;
  }
  .brand-name {
    color: var(--brand-grey);
    font-weight: 400;
    letter-spacing: 0.5px;
    line-height: 1.15;
  }
  .brand-name .line-main {
    display: block;
    font-size: 36px;
  }
  .brand-name .line-sub {
    display: block;
    font-size: 24px;
    padding-left: 96px;
  }
  .person {
    position: absolute;
    left: 23px;
    top: 423px;
    font-size: 20px;
    line-height: 34px;
  }
  .person-name {
    color: var(--ink);
    font-weight: 700;
  }
  .person-role {
    color: var(--orange);
  }
  .address {
    position: absolute;
    left: 368px;
    top: 421px;
    font-size: 20px;
    line-height: 36px;
    color: var(--grey);
  }
  .contact {
    position: absolute;
    left: 756px;
    top: 420px;
  }
  .contact-rule {
    position: absolute;
    left: 47px;
    top: 0;
    width: 1px;
    height: 134px;
    background: var(--rule);
  }
  .contact-row {
    display: flex;
    align-items: center;
    height: 48px;
    margin-bottom: 1px;
  }
  .contact-icon {
    width: 34px;
    height: 34px;
    display: flex;
    align-items: center;
    justify-content: center;
  }
  .contact-text {
    margin-left: 22px;
    font-size: 20px;
    color: var(--grey);
  }
  .web-band {
    position: absolute;
    left: 0;
    top: 603px;
    width: 1200px;
    height: 32px;
    background: linear-gradient(90deg, var(--yellow) 0, var(--yellow) 79px, var(--orange-light) 79px, var(--orange) 100%);
    display: flex;
    align-items: center;
    justify-content: center;
  }
  .web-address {
    color: var(--white);
    font-weight: 300;
    font-size: 22px;
    letter-spacing: 0.3px;
  }
</style>
</head>
<body>
<div class="card">
  <div class="brand">
    <div class="brand-dot"></div>
    <div class="brand-rule"></div>
    <div class="brand-name">
      <span class="line-main">KELVARA NORTH AUDIT</span>
      <span class="line-sub">&amp; COMPLIANCE</span>
    </div>
  </div>

  <div class="person">
    <div class="person-name">Name Surname</div>
    <div class="person-role">Position</div>
  </div>

  <div class="address">
    <div>Road 21st Suite 14,</div>
    <div>Sydney, Australia</div>
  </div>

  <div class="contact">
    <div class="contact-rule"></div>
    <div class="contact-row">
      <div class="contact-icon">
        <svg width="34" height="30" viewBox="0 0 34 30" aria-hidden="true">
          <path d="M5 3 C3 3 1 6 2 9 C5 18 12 25 21 28 C24 29 27 27 27 25 L27 22 L21 19 L18 22 C13 20 10 17 8 12 L11 9 L8 3 Z" fill="var(--orange)"/>
          <path d="M22 12 A4 4 0 0 1 26 16" stroke="var(--orange)" stroke-width="1.6" fill="none"/>
          <path d="M23 8 A8 8 0 0 1 30 15" stroke="var(--orange)" stroke-width="1.6" fill="none"/>
        </svg>
      </div>
      <span class="contact-text">1300 482 190</span>
    </div>
    <div class="contact-row">
      <div class="contact-icon">
        <svg width="20" height="34" viewBox="0 0 20 34" aria-hidden="true">
          <rect x="2" y="1.5" width="16" height="31" rx="3" fill="none" stroke="var(--orange)" stroke-width="2.4"/>
          <line x1="3" y1="6" x2="17" y2="6" stroke="var(--orange)" stroke-width="1.6"/>
          <line x1="3" y1="27" x2="17" y2="27" stroke="var(--orange)" stroke-width="1.6"/>
          <circle cx="10" cy="30" r="1.2" fill="var(--orange)"/>
        </svg>
      </div>
      <span class="contact-text">1300 482 190</span>
    </div>
    <div class="contact-row">
      <div class="contact-icon">
        <svg width="32" height="28" viewBox="0 0 32 28" aria-hidden="true">
          <path d="M1 11 L16 1 L31 11 L31 27 L1 27 Z" fill="var(--orange)"/>
          <path d="M5 10 L27 10 L27 17 L16 23 L5 17 Z" fill="var(--white)"/>
          <path d="M1 11 L16 21 L31 11" stroke="var(--orange)" stroke-width="2" fill="none"/>
        </svg>
      </div>
      <span class="contact-text">email.address@kelvaranorth.com.au</span>
    </div>
  </div>

  <div class="web-band">
    <span class="web-address">www.kelvaranorth.com.au</span>
  </div>
</div>
</body>
</html>
```